modern, IT themed business card for IT accelerator

Design a business card for tech oriented business accelerator. Prevailing color shall be orange.
we are operating in emerging markets and our mission is to provide co-working space, mentorship/coaching and ultimately seed financing IT startups.
also, we are helping financed ITs in obtaining next round financing, and to this end we are meeting with non IT/finance people and investment professionals..
that means card shall be designed to "impress" not only IT people (mostly liberal) but finance (more conservative)

Industry/Entity Type

Investment

Contact Information for Business Card

Company Name: Orin Founders Hub
Name: Levan Mordelashvili
Position: Partner
Address: 14, K Dorelani Ave., Tbilisi 0152, Georgia
Tel: +995591834467
Email: l.mordelashvili@orinhub.ge
Website: www.orinhub.ge

Font styles to use
Sans Serif

Requirements
Must have
• Attached are logos of the company (portrait & landscape) choose any
Nice to have
• industry is IT and finance (in fact, financing IT startups). therefore design might have IT theme (inspiration from web or software designs)

```html
<!DOCTYPE html>
<html lang="en">
<head>
<meta charset="utf-8">
<title>Orin Founders Hub – Business Card</title>
<link href="https://fonts.googleapis.com/css2?family=Montserrat:wght@400;700&display=swap" rel="stylesheet">
<style>
  :root {
    --bg: #e4e4e4;
    --paper: #f6f6f6;
    --orange: #e8740c;
    --grey: #8a8a8a;
    --white: #ffffff;
  }
  html, body {
    margin: 0;
    width: 1200px;
    height: 1200px;
    overflow: hidden;
    background: var(--bg);
    font-family: "Montserrat", sans-serif;
  }
  .card {
    position: absolute;
    left: 100px;
    top: 315px;
    width: 1000px;
    height: 570px;
    background: var(--paper);
    box-shadow: 0 2px 6px rgba(0,0,0,0.12);
    overflow: hidden;
  }
  .brand {
    position: absolute;
    left: 280px;
    top: 92px;
    display: flex;
    align-items: center;
    gap: 18px;
  }
  .brand-dot {
    width: 46px;
    height: 46px;
    border-radius: 50%;
    background: var(--orange);
  }
  .brand-rule {
    width: 3px;
    height: 80px;
    background: var(--orange);
  }
  .brand-name {
    font-size: 40px;
    font-weight: 400;
    color: var(--grey);
    letter-spacing: 0.5px;
  }
  .band {
    position: absolute;
    left: 0;
    top: 220px;
    width: 100%;
    height: 285px;
    background: var(--orange);
  }
  .person {
    position: absolute;
    left: 70px;
    bottom: 48px;
    color: var(--white);
  }
  .person-name {
    font-size: 34px;
    font-weight: 700;
    margin: 0;
  }
  .person-role {
    font-size: 26px;
    font-weight: 400;
    margin: 4px 0 0;
  }
  .contacts {
    position: absolute;
    left: 560px;
    top: 36px;
    margin: 0;
    padding: 0;
    list-style: none;
    color: var(--white);
    font-size: 24px;
    line-height: 1.3;
  }
  .contacts li {
    display: flex;
    align-items: flex-start;
    gap: 12px;
    margin-bottom: 8px;
  }
  .contacts svg {
    flex: none;
    width: 22px;
    height: 22px;
    margin-top: 4px;
  }
</style>
</head>
<body>
  <section class="card">
    <div class="brand">
      <span class="brand-dot"></span>
      <span class="brand-rule"></span>
      <span class="brand-name">Orin Founders Hub</span>
    </div>
    <div class="band">
      <ul class="contacts">
        <li>
          <svg viewBox="0 0 24 24" aria-hidden="true"><path fill="#fff" d="M12 2a7 7 0 0 0-7 7c0 5 7 13 7 13s7-8 7-13a7 7 0 0 0-7-7zm0 9.5A2.5 2.5 0 1 1 12 6.5a2.5 2.5 0 0 1 0 5z"/></svg>
          <span>14, K Dorelani Ave.,<br>Tbilisi 0152, Georgia</span>
        </li>
        <li>
          <svg viewBox="0 0 24 24" aria-hidden="true"><circle cx="12" cy="12" r="11" fill="#fff"/><path fill="#e8740c" d="M8.5 6.5l2 2.2-1.1 1.4c.8 1.7 2 2.9 3.6 3.7l1.4-1.1 2.2 2-1.2 1.8C11 16 8 13 6.8 8.2z"/></svg>
          <span>+995591834467</span>
        </li>
        <li>
          <svg viewBox="0 0 24 24" aria-hidden="true"><circle cx="12" cy="12" r="11" fill="#fff"/><rect x="6" y="8" width="12" height="8" fill="none" stroke="#e8740c" stroke-width="1.6"/><path d="M6 8l6 5 6-5" fill="none" stroke="#e8740c" stroke-width="1.6"/></svg>
          <span>l.mordelashvili@orinhub.ge</span>
        </li>
        <li>
          <svg viewBox="0 0 24 24" aria-hidden="true"><circle cx="12" cy="12" r="11" fill="#fff"/><g fill="none" stroke="#e8740c" stroke-width="1.4"><circle cx="12" cy="12" r="7"/><ellipse cx="12" cy="12" rx="3" ry="7"/><path d="M5 12h14"/></g></svg>
          <span>www.orinhub.ge</span>
        </li>
      </ul>
      <div class="person">
        <p class="person-name">Levan Mordelashvili</p>
        <p class="person-role">Partner</p>
      </div>
    </div>
  </section>
</body>
</html>
```